Burlgrain Joinery eye catching business card

I need an eye catching business card that reflects my traditional, fun, handmade woodcraft shop. I make high end custom furniture and fine woodworking products, a lot of which are rustic, natural looking. We are a small shop but we produce awesome, one of a kind wood products, and our business card should reflect that. Our target audience is young professionals to retired folks who want a quality, local, handmade product. I'd like the Shop Nearby logo somewhere on the card, BUT not overwhelming, the main focus is my Logo, no preference on color whichever looks the best. Visit my website to get a feel for my company. Burlgrainjoinery.com
Target Market(s)
young professionals to retired folks. Any one who wants to furnish their home with quality handcrafted products.
Industry/Entity Type
Business
Contact Information for Business Card
Dale Merriwick (555)417-6293
dale@burlgrainjoinery.com
www.burlgrainjoinery.com

```html
<!DOCTYPE html>
<html lang="en">
<head>
<meta charset="utf-8">
<title>Burlgrain Joinery – Business Card</title>
<link rel="stylesheet" href="https://fonts.googleapis.com/css2?family=Oswald:wght@500&family=Josefin+Sans:wght@600&display=swap">
<style>
  :root {
    --page-bg: #d9d6d2;
    --card-bg: #efefee;
    --wood-light: #b98350;
    --wood-mid: #9a6535;
    --wood-dark: #6f4422;
    --wood-ink: #4a2c14;
    --ink: #1b1b1b;
    --arc: #141414;
  }
  * { box-sizing: border-box; margin: 0; padding: 0; }
  html, body {
    width: 1200px; height: 970px; overflow: hidden;
    background: var(--page-bg);
  }
  .card {
    position: absolute; left: 100px; top: 207px;
    width: 1000px; height: 556px;
    background: var(--card-bg);
    box-shadow: 0 10px 30px rgba(0,0,0,.18);
    overflow: hidden;
  }
  .card__art { position: absolute; inset: 0; }
  .brand-side {
    position: absolute; left: 0; top: 0; width: 540px; height: 556px;
    text-align: center;
  }
  .brand-side__name {
    position: absolute; left: 0; right: 40px; top: 196px;
    font-family: "Oswald", sans-serif; font-weight: 500;
    color: var(--wood-ink);
    font-size: 58px; line-height: 62px; letter-spacing: 3px;
    text-transform: uppercase;
  }
  .brand-side__web {
    position: absolute; left: 0; right: 40px; top: 404px;
    font-family: "Oswald", sans-serif; font-weight: 500;
    color: var(--wood-ink);
    font-size: 28px; letter-spacing: .5px;
  }
  .info-side {
    position: absolute; left: 560px; top: 0; width: 440px; height: 556px;
  }
  .info-side__brand {
    position: absolute; left: 0; right: 0; top: 62px; text-align: center;
    font-family: "Oswald", sans-serif; font-weight: 500;
    color: var(--ink);
    font-size: 44px; line-height: 50px; letter-spacing: 3px;
    text-transform: uppercase;
  }
  .info-side__tagline {
    position: absolute; left: 0; right: 0; top: 214px; text-align: center;
    font-family: "Josefin Sans", sans-serif; font-weight: 600;
    color: var(--ink);
    font-size: 11px; letter-spacing: 1.5px; text-transform: uppercase;
  }
  .contact {
    position: absolute; left: 38px; top: 350px;
    font-family: "Oswald", sans-serif; font-weight: 500; color: var(--ink);
    list-style: none;
  }
  .contact__name { font-size: 32px; letter-spacing: 1px; margin-bottom: 16px; }
  .contact__line {
    display: flex; align-items: center; gap: 12px;
    font-size: 24px; letter-spacing: 1px; margin-bottom: 12px;
  }
  .contact__icon { width: 22px; height: 18px; flex: none; }
</style>
</head>
<body>
  <article class="card">
    <svg class="card__art" width="1000" height="556" viewBox="0 0 1000 556">
      <defs>
        <linearGradient id="woodTone" x1="0" y1="0" x2="1" y2="1">
          <stop offset="0" stop-color="var(--wood-mid)"/>
          <stop offset=".45" stop-color="var(--wood-light)"/>
          <stop offset="1" stop-color="var(--wood-dark)"/>
        </linearGradient>
        <clipPath id="woodShape">
          <circle cx="184" cy="278" r="364"/>
        </clipPath>
      </defs>
      <rect class="wood-panel" role="img" aria-label="Wood plank grain texture"
            x="0" y="0" width="560" height="556" fill="url(#woodTone)" clip-path="url(#woodShape)"/>
      <circle class="divider-arc" cx="184" cy="278" r="382" fill="none" stroke="var(--arc)" stroke-width="10"/>
    </svg>

    <section class="brand-side">
      <h1 class="brand-side__name">Burlgrain<br>Joinery</h1>
      <p class="brand-side__web">www.burlgrainjoinery.com</p>
    </section>

    <section class="info-side">
      <p class="info-side__brand">Burlgrain<br>Joinery</p>
      <p class="info-side__tagline">Handmade in Alder Creek, OR</p>
      <ul class="contact">
        <li class="contact__name">Dale Merriwick</li>
        <li class="contact__line">
          <svg class="contact__icon" viewBox="0 0 22 18" aria-hidden="true">
            <path d="M1 6 Q11 -1 21 6 L18 8 L15 5 L7 5 L4 8 Z" fill="var(--ink)"/>
            <path d="M6 8 L16 8 L19 16 L3 16 Z" fill="var(--ink)"/>
            <circle cx="11" cy="12" r="2.2" fill="var(--card-bg)"/>
          </svg>
          (555)417-6293
        </li>
        <li class="contact__line">
          <svg class="contact__icon" viewBox="0 0 22 18" aria-hidden="true">
            <rect x="1" y="3" width="20" height="13" fill="var(--ink)"/>
            <path d="M1.5 3.5 L11 11 L20.5 3.5" fill="none" stroke="var(--card-bg)" stroke-width="1.5"/>
          </svg>
          dale@burlgrainjoinery.com
        </li>
      </ul>
    </section>
  </article>
</body>
</html>
```